Marlowe Holdings LLC - Business Cards

Need the following information on the cards:

Name: Dean R Vossler
Title: Chief Executive Manager

Business address:
412 N Ridgeview Lane #118
Carol Stream, Il 60412

Phone: (630) 555-0148 - Business
KPV FFL license number: 5-21-xxx-xx-xx-04519
Email: dean.vossler@marloweholdingsffl.com

Target Market(s)

Firearm owners

Industry/Entity Type

Firearms industry,

Contact Information for Business Card

Contact number, name and title, web page address, email, business address and kpv license number,

Requirements
Must have
• Name, title, business address, phone numbers, KPV license numbers, web page address and email address.
Nice to have
• Cellphone number,

```html
<!DOCTYPE html>
<html lang="en">
<head>
<meta charset="utf-8">
<title>Marlowe Holdings LLC – Business Cards</title>
<link rel="stylesheet" href="https://fonts.googleapis.com/css2?family=Arimo:wght@400;700&display=swap">
<style>
  :root {
    --stage: #3b3b3d;
    --card: #2a2a2c;
    --card-edge: #1f1f21;
    --accent-red: #b3141c;
    --text-light: #e6e6e6;
    --text-muted: #cfcfcf;
    --rule: #9a9a9a;
    --emboss-dark: #1c1c1e;
    --emboss-light: #343437;
  }
  * { box-sizing: border-box; margin: 0; padding: 0; }
  html, body { width: 1200px; height: 900px; overflow: hidden; }
  body {
    background: var(--stage);
    font-family: "Arimo", Arial, sans-serif;
    display: flex;
    flex-direction: column;
    align-items: center;
    justify-content: center;
    gap: 28px;
  }
  .card {
    position: relative;
    width: 720px;
    height: 411px;
    background: linear-gradient(135deg, #2f2f31 0%, var(--card) 55%, var(--card-edge) 100%);
    border-bottom: 4px solid var(--accent-red);
    box-shadow: 0 10px 24px rgba(0,0,0,.45);
    overflow: hidden;
  }

  /* Contact side */
  .contact-card .brand-block {
    position: absolute;
    left: 50px; top: 95px;
    width: 250px; height: 220px;
    display: flex; flex-direction: column;
    align-items: center; justify-content: center;
    gap: 18px;
  }
  .brand-dot {
    width: 120px; height: 120px;
    border: 3px solid var(--text-light);
    border-radius: 50%;
  }
  .brand-name {
    color: var(--accent-red);
    font-weight: 700;
    font-size: 20px;
    letter-spacing: 1.5px;
    text-transform: uppercase;
    text-align: center;
  }
  .divider {
    position: absolute;
    left: 330px; top: 60px;
    width: 1.5px; height: 290px;
    background: var(--rule);
  }
  .details {
    position: absolute;
    left: 355px; top: 70px;
    right: 16px;
    color: var(--text-muted);
    font-size: 15px;
    line-height: 1.35;
  }
  .details .person-name {
    color: var(--accent-red);
    font-weight: 700;
    font-size: 19px;
    text-transform: uppercase;
    letter-spacing: .5px;
  }
  .details .person-title { margin-bottom: 14px; }
  .details .address { margin-bottom: 14px; }
  .contact-line { display: flex; align-items: center; gap: 9px; white-space: nowrap; }
  .contact-line svg { width: 15px; height: 15px; flex: none; }
  .license { margin-top: 14px; }

  /* Brand side */
  .brand-card .wordmark {
    position: absolute;
    left: 70px; top: 178px;
    color: var(--accent-red);
    font-weight: 700;
    font-size: 36px;
    letter-spacing: 3px;
    text-transform: uppercase;
  }
  .brand-card .emboss-art {
    position: absolute;
    right: 0; top: 0;
    width: 330px; height: 100%;
    background: radial-gradient(ellipse at 55% 50%, var(--emboss-light) 0%, var(--emboss-dark) 70%, transparent 100%);
    opacity: .9;
  }
</style>
</head>
<body>

  <section class="card contact-card">
    <div class="brand-block">
      <div class="brand-dot"></div>
      <div class="brand-name">Marlowe Holdings LLC</div>
    </div>
    <div class="divider"></div>
    <div class="details">
      <p class="person-name">Dean R Vossler</p>
      <p class="person-title">Chief Executive Manager</p>
      <p class="address">412 N Ridgeview Lane #118<br>Carol Stream, IL 60412</p>
      <p class="contact-line">
        <svg viewBox="0 0 16 16" aria-hidden="true"><circle cx="8" cy="8" r="8" fill="var(--accent-red)"/><path d="M5 4.5c.5 3 2.5 5.5 6 6.8l.8-1.6-1.8-1-1 1c-1.2-.6-2-1.5-2.5-2.6l1-.9-.9-1.9z" fill="#fff"/></svg>
        (630) 555-0148
      </p>
      <p class="contact-line">
        <svg viewBox="0 0 16 16" aria-hidden="true"><rect x="1" y="3" width="14" height="10" fill="var(--accent-red)"/><path d="M1 3l7 5.5L15 3" stroke="#fff" stroke-width="1.3" fill="none"/></svg>
        dean.vossler@marloweholdingsffl.com
      </p>
      <p class="contact-line">
        <svg viewBox="0 0 16 16" aria-hidden="true"><circle cx="8" cy="8" r="7.5" fill="var(--accent-red)"/><circle cx="8" cy="8" r="4.5" stroke="#fff" stroke-width="1.2" fill="none"/><path d="M3.5 8h9M8 3.5v9" stroke="#fff" stroke-width="1.2"/></svg>
        www.marloweholdingsffl.com
      </p>
      <p class="license">KPV FFL: 5-21-xxx-xx-xx-04519</p>
    </div>
  </section>

  <section class="card brand-card">
    <div class="emboss-art" role="img" aria-label="Embossed crossed rifles illustration in dark tone-on-tone"></div>
    <div class="wordmark">Marlowe Holdings LLC</div>
  </section>

</body>
</html>
```